Kestrelway Advisory logo/business card design -- a digital consulting company

I've just restarted a consulting company I had years ago--Kestrelway Advisory. Now I need a new business card and updated logo. The original logo was simple enough: a chart-like progression atop a grid (see the attached file). I do strategy work, and the chart is meant to show incremental growth and profit. I'd like the reincarnation of my logo to be 3D, with both the grid and arrow rotated on their axis.

I'll want to use the logo on my website as well. I'm open to color schemes, fonts, etc.

Target Market(s)

Business-to-Business. Target market is corporate.

Industry/Entity Type

Business

Contact Information for Business Card

Logo on one-side; name and other contact info on the back

Font styles to use
Serif
Sans Serif

Requirements
Nice to have
• Kestrelway Advisory refers to the concept of "bootstrapping" or making incremental changes to grow with minimal risk and financial exposure, and self-sufficiency (think of the phrase "to pull oneself by one's bootstraps.")

```html
<!DOCTYPE html>
<html lang="en">
<head>
<meta charset="UTF-8">
<title>Kestrelway Advisory – Business Card</title>
<link rel="stylesheet" href="https://fonts.googleapis.com/css2?family=Montserrat:wght@400;600&display=swap">
<style>
  :root {
    --backdrop: #e2e2e2;
    --card-light: #ffffff;
    --card-dark: #232323;
    --ink: #141414;
    --ink-soft: #555555;
    --accent: #4b3f9c;
    --on-dark: #f2f2f2;
  }
  * { margin: 0; padding: 0; box-sizing: border-box; }
  html, body {
    width: 1200px; height: 900px; overflow: hidden;
    background: var(--backdrop);
    font-family: "Montserrat", sans-serif;
  }
  .canvas { position: relative; width: 1200px; height: 900px; }
  .card {
    position: absolute; left: 274px; width: 623px; height: 365px;
    overflow: hidden;
    box-shadow: 0 2px 6px rgba(0,0,0,0.25);
  }
  .card--front { top: 55px; background: var(--card-light); }
  .card--back { top: 473px; background: var(--card-dark); }

  .brand { position: absolute; display: flex; align-items: center; }
  .brand__square { background: var(--accent); flex: none; }
  .brand__name { font-weight: 400; text-transform: uppercase; white-space: nowrap; }

  .card--front .brand { left: 58px; top: 166px; gap: 12px; }
  .card--front .brand__square { width: 26px; height: 26px; }
  .card--front .brand__name { font-size: 15px; letter-spacing: 2px; color: var(--ink-soft); }

  .card--back .brand { left: 124px; top: 155px; gap: 20px; }
  .card--back .brand__square { width: 58px; height: 58px; }
  .card--back .brand__name { font-size: 22px; letter-spacing: 2px; color: var(--on-dark); }

  .contact { position: absolute; left: 363px; top: 112px; color: var(--ink); }
  .contact__name { font-size: 22px; font-weight: 400; line-height: 1.1; }
  .contact__name strong { font-weight: 600; }
  .contact__title { font-size: 16px; color: var(--accent); margin-top: 3px; }
  .contact__list { list-style: none; margin-top: 16px; }
  .contact__item {
    display: flex; align-items: center; gap: 9px;
    font-size: 14.5px; height: 26.5px;
  }
  .contact__icon { width: 15px; height: 15px; flex: none; fill: var(--accent); }
  .contact__icon--outline { fill: none; stroke: var(--accent); stroke-width: 1.1; }
</style>
</head>
<body>
<main class="canvas">
  <section class="card card--front" aria-label="Card front">
    <div class="brand">
      <span class="brand__square"></span>
      <span class="brand__name">Kestrelway Advisory</span>
    </div>
    <div class="contact">
      <p class="contact__name"><strong>Your</strong> Name</p>
      <p class="contact__title">Job Title</p>
      <ul class="contact__list">
        <li class="contact__item">
          <svg class="contact__icon" viewBox="0 0 16 16" aria-hidden="true"><path d="M1 6c0-2 3-3 7-3s7 1 7 3v1h-3V5.5H4V7H1z"/><path d="M3 8h10l1 5H2z"/></svg>
          <span>000 000 0000</span>
        </li>
        <li class="contact__item">
          <svg class="contact__icon" viewBox="0 0 16 16" aria-hidden="true"><path d="M1 4h14v9H1z"/><path d="M1.5 4.5 8 9l6.5-4.5" stroke="#fff" stroke-width="1.2" fill="none"/></svg>
          <span>youremail@xyz.com</span>
        </li>
        <li class="contact__item">
          <svg class="contact__icon contact__icon--outline" viewBox="0 0 16 16" aria-hidden="true"><circle cx="8" cy="8" r="6.5"/><ellipse cx="8" cy="8" rx="3" ry="6.5"/><path d="M1.5 8h13M2.5 5h11M2.5 11h11"/></svg>
          <span>www.yourwebsite.come</span>
        </li>
      </ul>
    </div>
  </section>

  <section class="card card--back" aria-label="Card back">
    <div class="brand">
      <span class="brand__square"></span>
      <span class="brand__name">Kestrelway Advisory</span>
    </div>
  </section>
</main>
</body>
</html>
```